Packaging for nuts & dried fruits products

We need a packaging design for our nuts and dried fruits product in a stand-up pouch with 23x13cm size. We repack and/or process almonds, sliced almonds, walnuts, pistachios, cashews, dried blueberries, dried cranberries, and dried mangoes. We need the design to look fresh, premium, and professional. We would like to see designs that use color green but with color combinations of either beige, gray, or black.

See on the upload files a sample of what we've initially done. NOTE that the white space on the front will be a "window" where the products can be seen by consumers and the design/colors used to be catchy.

The challenge here is the product name (ex. Walnuts) will NOT be printed on the packaging itself but will be labelled using stickers - meaning this will be a generic template for all our products.

TK Back and TK_Front images are our initial designs, while the rest are images from the internet for references.

Target Market(s)

Market are for athletic individuals, health conscious, fresh/organic food buyers.
Middle to upper market.

Industry/Entity Type

Product

Colors
abd036
9bcb3c

Requirements
Must have
• 1. A "window" or see through area for the product.
• 2. Healthy, fresh, and natural concept.
• 3. There must be a FRONT and BACK design submitted.
• 4. Design must be appropriate for printing on a Stand-up resealable pouch (see uploaded Sample_packaging.jpg).
• 5. All information at TK_Back image must be on back design as well.
• 6. Storage and Allergy information must be at the back.
• 7. Leave an area for barcode.
Nice to have
• 1. Outlines/emboss of nuts (walnuts, cashews, almonds, pistachios, blueberries, cranberries).
• 2. Put "Great for snacks and baking!" at the front.
• 3. Put "Resealable to contain freshness" at the top of the packaging.
Should not have
• 1. Should not have a product label or packaging size on the design (ex. Walnuts 500g).
• 2. Should not use "heart" shapes.

```html
<!DOCTYPE html>
<html lang="en">
<head>
<meta charset="utf-8">
<title>Stand-up Pouch Front – Nuts &amp; Dried Fruits</title>
<link rel="stylesheet" href="https://fonts.googleapis.com/css2?family=Lilita+One&family=Arimo:wght@400;700&display=swap">
<style>
  :root {
    --stage-bg: #eeeeea;
    --pouch-white: #ffffff;
    --green-side: #9bcb3c;
    --green-main: #abd036;
    --green-label: #c6dc5c;
    --label-dash: #6d7a2a;
    --maroon: #6a1b14;
    --ink: #1a1a1a;
    --nut-light: #d9a56a;
    --nut-mid: #a8642f;
    --nut-dark: #6e3a1c;
  }
  * { margin: 0; padding: 0; box-sizing: border-box; }
  html, body {
    width: 1200px; height: 691px; overflow: hidden;
    background: var(--stage-bg);
  }
  .pouch-front {
    position: absolute; left: 380px; top: 45px;
    width: 440px; height: 600px;
    background: var(--pouch-white);
    box-shadow: 0 14px 30px rgba(0,0,0,0.22);
    overflow: hidden;
  }
  .artwork { position: absolute; inset: 0; }
  .side-pattern { position: absolute; top: 0; height: 100%; }
  .reseal-tag {
    position: absolute; left: 93px; top: 63px; width: 217px; height: 19px;
    border: 1px solid var(--label-dash);
    font: 700 10.5px/17px "Arimo", sans-serif;
    color: var(--ink); text-align: center; letter-spacing: 0.2px;
    font-style: italic;
  }
  .logo-space {
    position: absolute; left: 83px; width: 241px; top: 138px;
    font: 400 22px/28px "Arimo", sans-serif;
    color: var(--ink); text-align: center;
  }
  .claim-label {
    position: absolute; left: 70px; top: 200px; width: 262px; height: 180px;
    background: var(--green-label);
    transform: rotate(-5deg);
    padding: 7px;
  }
  .claim-label .dash-frame {
    width: 100%; height: 100%;
    border: 1.5px dashed var(--label-dash);
    display: flex; align-items: center; justify-content: center;
  }
  .claim-text {
    font: 400 40px/44px "Lilita One", sans-serif;
    color: var(--maroon); text-align: center; letter-spacing: 0.5px;
  }
  .window-note {
    position: absolute; left: 0; width: 100%; top: 561px;
    font: 400 20px/26px "Arimo", sans-serif;
    color: var(--ink); text-align: center;
  }
</style>
</head>
<body>
  <div class="pouch-front">
    <svg class="artwork" width="440" height="600" viewBox="0 0 440 600" aria-hidden="true">
      <defs>
        <clipPath id="window-edge">
          <path d="M0,0 H440 V470 C420,462 400,476 380,470 C350,462 330,490 300,484 C275,480 255,492 245,508 C238,520 232,532 220,536 C208,532 202,520 195,508 C185,492 165,480 140,484 C110,490 90,462 60,470 C40,476 20,440 0,446 Z"/>
        </clipPath>
        <linearGradient id="nut-tone" x1="0" y1="0" x2="1" y2="1">
          <stop offset="0" stop-color="var(--nut-light)"/>
          <stop offset="0.5" stop-color="var(--nut-mid)"/>
          <stop offset="1" stop-color="var(--nut-dark)"/>
        </linearGradient>
      </defs>
      <g clip-path="url(#window-edge)">
        <rect x="0" y="0" width="440" height="600" fill="var(--green-side)"/>
        <rect x="83" y="0" width="241" height="600" fill="var(--green-main)"/>
      </g>
    </svg>

    <div class="side-pattern" style="left:0;width:83px;height:380px" role="img" aria-label="Line drawings of nuts and seeds on green"></div>
    <div class="side-pattern" style="left:324px;width:116px;height:380px" role="img" aria-label="Line drawings of nuts and seeds on green"></div>

    <div class="reseal-tag">RESEALABLE TO CONTAIN FRESHNESS</div>
    <div class="logo-space">Space for Logo</div>

    <div class="claim-label">
      <div class="dash-frame">
        <p class="claim-text">GREAT FOR<br>SNACKS &amp;<br>BAKING!</p>
      </div>
    </div>

    <svg class="artwork" width="440" height="600" viewBox="0 0 440 600" role="img" aria-label="Photo of mixed almonds, walnuts, cashews and blueberries with leaves">
      <path fill="url(#nut-tone)" d="M0,428 C40,400 90,392 140,386 C200,380 260,384 320,390 C370,396 410,404 440,414 V470 C420,462 400,476 380,470 C350,462 330,490 300,484 C275,480 255,492 245,508 C238,520 232,532 220,536 C208,532 202,520 195,508 C185,492 165,480 140,484 C110,490 90,462 60,470 C40,476 20,440 0,446 Z"/>
    </svg>

    <p class="window-note">see through area for the product</p>
  </div>
</body>
</html>
```